2-page digital brochure highlighting company and service offerings to oil and gas market in W Canada

we are asked to send a quick info package to potential clients. Brief description of who Northbend Conduit Corp is and what we can offer our Oil & Gas, Midstream and engineering prospects. Our services include ; pipeline maintenance and integrity, abandonments and decommissioning, and project management. PP attached for pictures and verbiage. Branding guidelines below. want to promote services and safety

```html
<!DOCTYPE html>
<html lang="en">
<head>
<meta charset="utf-8">
<title>Northbend Conduit Corp – Brochure</title>
<link rel="stylesheet" href="https://fonts.googleapis.com/css2?family=Roboto:ital,wght@0,400;0,700;0,900;1,400;1,700&family=Montserrat:wght@700&family=Allura&display=swap">
<style>
  :root{
    --navy:#0a4a6c;
    --orange:#e8902a;
    --orange-soft:#f0a23a;
    --ink:#111;
    --paper:#ffffff;
    --backdrop:#dedcd9;
  }
  html,body{margin:0;padding:0;width:764px;height:1200px;overflow:hidden;background:var(--backdrop);}
  .page{position:absolute;left:178px;width:408px;height:576px;background:var(--paper);box-shadow:0 10px 24px rgba(0,0,0,.22);}
  .page--cover{top:16px;}
  .page--services{top:608px;}
  .page svg{display:block;width:408px;height:576px;}
  .sans{font-family:"Roboto",Arial,sans-serif;}
  .brand{font-family:"Montserrat","Roboto",sans-serif;font-weight:700;}
  .script{font-family:"Allura",cursive;}
  .b{font-weight:700;}
  .headline{font-size:34px;fill:var(--navy);}
  .tagline{font-size:30px;fill:var(--navy);}
  .motto{font-size:31px;font-weight:700;font-style:italic;fill:var(--orange);}
  .origin{font-size:20px;font-style:italic;fill:var(--navy);}
  .cell-title{font-size:20px;}
  .on-blue{fill:#fff;}
  .on-white{fill:var(--navy);}
  .intro{font-size:13.4px;fill:#fff;}
  .icon-o{fill:var(--orange);}
  .icon-w{fill:#fff;}
  .line-o{fill:none;stroke:var(--orange);stroke-width:5;stroke-linecap:round;}
  .line-w{fill:none;stroke:#fff;stroke-width:5;stroke-linecap:round;}
  .cut-b{fill:var(--navy);}
  .cut-w{fill:#fff;}
</style>
</head>
<body>

<section class="page page--cover">
<svg viewBox="0 0 675 953" xmlns="http://www.w3.org/2000/svg">
  <defs>
    <linearGradient id="frameTone" x1="0" y1="0" x2="1" y2="1">
      <stop offset="0" stop-color="#1d5f80"/>
      <stop offset="1" stop-color="#6b98ad"/>
    </linearGradient>
    <linearGradient id="workerTone" x1="0" y1="0" x2="1" y2="1">
      <stop offset="0" stop-color="#e7873a"/>
      <stop offset=".5" stop-color="#3c5a3e"/>
      <stop offset="1" stop-color="#8c8f7a"/>
    </linearGradient>
    <clipPath id="pageClip"><rect width="675" height="953"/></clipPath>
  </defs>

  <g class="logo">
    <rect x="46" y="58" width="40" height="40" fill="var(--navy)"/>
    <text class="brand" x="98" y="88" font-size="26" fill="var(--navy)">Northbend</text>
  </g>

  <g transform="rotate(-4 133 165)">
    <rect x="38" y="140" width="190" height="50" fill="var(--orange)"/>
    <text class="sans b" x="52" y="178" font-size="28" fill="#fff">OUR VISION</text>
  </g>

  <text class="sans headline">
    <tspan x="46" y="232">Is To Be <tspan class="b">North</tspan></tspan>
    <tspan x="46" y="269" class="b">America’s Premier</tspan>
    <tspan x="46" y="306" class="b">Pipeline Integrity</tspan>
    <tspan x="46" y="343">Maintenance</tspan>
  </text>
  <g class="script" fill="var(--orange)">
    <text x="48" y="378" font-size="46" transform="rotate(-6 48 378)">Service</text>
    <text x="62" y="438" font-size="64" transform="rotate(-6 62 438)">Provider!</text>
  </g>

  <polygon role="img" aria-label="Photo of a pipeline worker in hard hat and safety vest tightening a valve" points="352,290 568,68 675,170 675,330 515,465" fill="url(#workerTone)"/>
  <polygon points="605,282 675,212 675,350" fill="var(--orange)"/>

  <g clip-path="url(#pageClip)">
    <polygon role="img" aria-label="Blue-toned photo of pipeline coating work" points="250,430 553,720 250,1010 -50,720" fill="url(#frameTone)"/>
    <polygon role="img" aria-label="Orange-toned photo detail" points="60,600 180,720 60,840 -60,720" fill="var(--orange-soft)"/>
    <polygon points="250,530 445,720 250,910 55,720" fill="#fff"/>
  </g>

  <ellipse role="img" aria-label="Illustration of a yellow hard hat" cx="80" cy="510" rx="55" ry="42" fill="#e6a93a"/>
  <rect role="img" aria-label="Illustration of a yellow pipe with red valve" x="445" y="520" width="170" height="36" rx="8" fill="#e9b52a"/>

  <text class="sans tagline" text-anchor="middle">
    <tspan x="250" y="668">The Northbend</tspan>
    <tspan x="250" y="701">Story</tspan>
  </text>
  <text class="sans motto" text-anchor="middle">
    <tspan x="250" y="742">Focused. Safe.</tspan>
    <tspan x="250" y="780">Collaborative.</tspan>
  </text>

  <text class="sans origin">
    <tspan x="448" y="846">Northbend Conduit</tspan>
    <tspan x="448" y="868">Corp. (NCC) is borne</tspan>
    <tspan x="448" y="890">out of a belief in</tspan>
    <tspan x="448" y="912">executing differently.</tspan>
  </text>
</svg>
</section>

<section class="page page--services">
<svg viewBox="0 0 675 953" xmlns="http://www.w3.org/2000/svg">
  <defs>
    <symbol id="chev-o" viewBox="0 0 20 24"><path d="M4 2 L16 12 L4 22" fill="none" stroke="var(--orange)" stroke-width="5"/></symbol>
    <symbol id="chev-k" viewBox="0 0 20 24"><path d="M4 2 L16 12 L4 22" fill="none" stroke="var(--ink)" stroke-width="5"/></symbol>
    <symbol id="gear" viewBox="-40 -40 80 80">
      <circle r="26"/>
      <rect x="-7" y="-37" width="14" height="74"/>
      <rect x="-37" y="-7" width="74" height="14"/>
      <rect x="-7" y="-37" width="14" height="74" transform="rotate(45)"/>
      <rect x="-7" y="-37" width="14" height="74" transform="rotate(-45)"/>
    </symbol>
  </defs>

  <!-- header cell -->
  <rect role="img" aria-label="Illustration of a red power drill" x="22" y="26" width="88" height="52" rx="10" fill="#d8383a" opacity=".85"/>
  <g transform="translate(138 135)">
    <use href="#gear" x="-30" y="-30" width="60" height="60" fill="var(--orange)"/>
    <circle r="10" fill="#fff"/>
  </g>
  <text class="sans b" x="138" y="200" font-size="38" text-anchor="middle" fill="var(--navy)">Services</text>

  <!-- intro cell -->
  <rect x="238" y="37" width="199" height="220" fill="var(--navy)"/>
  <text class="sans intro">
    <tspan x="255" y="72">Northbend service offerings</tspan>
    <tspan x="255" y="87">provide a multi faceted</tspan>
    <tspan x="255" y="102">team experienced at scope</tspan>
    <tspan x="255" y="117">and sequencing programs</tspan>
    <tspan x="255" y="132">related to maintaining or</tspan>
    <tspan x="255" y="147">retiring oil and gas</tspan>
    <tspan x="255" y="162">infrastructure and assets.</tspan>
  </text>
  <use href="#chev-o" x="390" y="192" width="22" height="28"/>

  <!-- blue tiles -->
  <g fill="var(--navy)">
    <rect x="40" y="257" width="199" height="220"/>
    <rect x="437" y="257" width="198" height="220"/>
    <rect x="238" y="476" width="199" height="220"/>
    <rect x="40" y="696" width="199" height="220"/>
    <rect x="437" y="696" width="198" height="220"/>
  </g>

  <!-- Repair and Rehabilitation -->
  <text class="sans cell-title on-white"><tspan x="454" y="77"><tspan class="b">Repair</tspan> and</tspan><tspan x="454" y="98" class="b">Rehabilitation</tspan></text>
  <g class="icon-o" aria-hidden="true">
    <rect x="542" y="158" width="10" height="12"/>
    <rect x="532" y="154" width="30" height="6" rx="2"/>
    <rect x="512" y="172" width="70" height="22" rx="4"/>
    <rect x="507" y="168" width="8" height="30"/>
    <rect x="579" y="168" width="8" height="30"/>
    <rect x="520" y="206" width="54" height="10" rx="5"/>
    <circle cx="517" cy="211" r="12"/>
    <circle cx="577" cy="211" r="12"/>
    <rect x="508" y="206" width="10" height="10" class="cut-w"/>
    <rect x="576" y="206" width="10" height="10" class="cut-w"/>
  </g>
  <use href="#chev-k" x="600" y="198" width="16" height="20"/>

  <!-- Integrity Verification Dig -->
  <text class="sans cell-title on-blue"><tspan x="65" y="302" class="b">Integrity</tspan><tspan x="65" y="323" class="b">Verification</tspan><tspan x="65" y="344">Dig</tspan></text>
  <g aria-hidden="true">
    <circle cx="117" cy="392" r="11" class="icon-w"/>
    <rect x="112" y="380" width="10" height="8" class="cut-b"/>
    <rect x="112" y="398" width="10" height="42" class="icon-w"/>
    <path d="M135 384 q8 -6 16 0 q8 6 16 0 q8 -6 16 0 v6 h-48z" class="icon-w"/>
    <rect x="135" y="393" width="48" height="47" class="icon-w"/>
    <rect x="144" y="393" width="3" height="47" class="cut-b"/>
    <rect x="157" y="393" width="3" height="47" class="cut-b"/>
    <rect x="170" y="393" width="3" height="47" class="cut-b"/>
  </g>
  <use href="#chev-o" x="198" y="415" width="16" height="20"/>

  <!-- Program Management and Execution -->
  <text class="sans cell-title on-white"><tspan x="254" y="302">Program</tspan><tspan x="254" y="323" class="b">Management</tspan><tspan x="254" y="344">and <tspan class="b">Execution</tspan></tspan></text>
  <g aria-hidden="true">
    <rect x="312" y="378" width="30" height="34" rx="2" class="icon-o"/>
    <rect x="317" y="386" width="20" height="3" class="cut-w"/>
    <rect x="317" y="393" width="20" height="3" class="cut-w"/>
    <rect x="317" y="400" width="14" height="3" class="cut-w"/>
    <use href="#gear" x="348" y="376" width="36" height="36" class="icon-o"/>
    <circle cx="366" cy="394" r="6" class="cut-w"/>
    <rect x="314" y="416" width="66" height="28" rx="14" class="icon-o"/>
    <rect x="334" y="416" width="3" height="28" class="cut-w"/>
    <rect x="356" y="416" width="3" height="28" class="cut-w"/>
  </g>
  <use href="#chev-k" x="397" y="415" width="16" height="20"/>

  <!-- Watercourse Crossing Repair -->
  <text class="sans cell-title on-blue"><tspan x="455" y="306" class="b">Watercourse</tspan><tspan x="455" y="327"><tspan class="b">Crossing</tspan> Repair</tspan></text>
  <g aria-hidden="true">
    <path d="M531 378 h28 v14 q0 12 -14 18 q-14 -6 -14 -18z" class="line-w" stroke-width="4"/>
    <rect x="500" y="418" width="90" height="20" class="icon-w"/>
    <rect x="510" y="414" width="4" height="28" class="cut-b"/>
    <rect x="576" y="414" width="4" height="28" class="cut-b"/>
    <path d="M538 416 l6 10 l-6 12 h3 l6 -12 l-6 -10z" class="cut-b"/>
  </g>
  <use href="#chev-o" x="600" y="415" width="16" height="20"/>

  <!-- Engineering and Project Management -->
  <text class="sans cell-title on-white"><tspan x="65" y="521" class="b">Engineering</tspan><tspan x="65" y="542">and <tspan class="b">Project</tspan></tspan><tspan x="65" y="563">Management</tspan></text>
  <g aria-hidden="true">
    <rect x="105" y="590" width="60" height="80" rx="4" class="icon-o"/>
    <rect x="122" y="584" width="26" height="12" rx="3" class="icon-o"/>
    <path d="M115 612 l6 6 l10 -12" class="line-w" stroke-width="4"/>
    <rect x="137" y="608" width="20" height="4" class="cut-w"/>
    <path d="M115 634 l6 6 l10 -12" class="line-w" stroke-width="4"/>
    <rect x="137" y="630" width="20" height="4" class="cut-w"/>
    <path d="M115 656 l6 6 l10 -12" class="line-w" stroke-width="4"/>
    <rect x="137" y="652" width="20" height="4" class="cut-w"/>
  </g>
  <use href="#chev-k" x="198" y="633" width="16" height="20"/>

  <!-- In-line Inspection Program Support -->
  <text class="sans cell-title on-blue"><tspan x="254" y="521" class="b">In-line</tspan><tspan x="254" y="542" class="b">Inspection</tspan><tspan x="254" y="563">Program Support</tspan></text>
  <g aria-hidden="true">
    <circle cx="335" cy="615" r="22" class="line-w" stroke-width="5"/>
    <line x1="318" y1="630" x2="304" y2="650" class="line-w" stroke-width="7"/>
    <rect x="292" y="656" width="90" height="20" class="icon-w"/>
    <rect x="302" y="652" width="4" height="28" class="cut-b"/>
    <rect x="330" y="660" width="20" height="12" rx="6" class="cut-b"/>
    <rect x="368" y="652" width="4" height="28" class="cut-b"/>
  </g>
  <use href="#chev-o" x="397" y="633" width="16" height="20"/>

  <!-- HDD Support -->
  <text class="sans cell-title on-white"><tspan x="455" y="521" class="b">HDD</tspan><tspan x="455" y="542">Support</tspan></text>
  <rect role="img" aria-label="Illustration of a red drill bit" x="585" y="462" width="58" height="80" rx="10" fill="#c9363a" opacity=".8"/>
  <g aria-hidden="true">
    <rect x="490" y="640" width="50" height="26" rx="3" class="icon-o"/>
    <path d="M540 666 l44 -58" class="line-o" stroke-width="6"/>
    <path d="M560 666 l24 -58" class="line-o" stroke-width="4"/>
    <rect x="486" y="668" width="104" height="6" class="icon-o"/>
  </g>
  <use href="#chev-k" x="600" y="633" width="16" height="20"/>

  <!-- Geohazard Management -->
  <text class="sans cell-title on-blue"><tspan x="65" y="741" class="b">Geohazard</tspan><tspan x="65" y="762">Management</tspan></text>
  <g aria-hidden="true" class="icon-w">
    <polygon points="110,825 172,895 110,895"/>
    <polygon points="128,822 138,818 142,828 132,832"/>
    <polygon points="146,840 156,836 160,846 150,850"/>
    <polygon points="162,862 170,858 173,866 165,869"/>
  </g>
  <use href="#chev-o" x="198" y="860" width="16" height="20"/>

  <!-- Coating Application -->
  <text class="sans cell-title on-white"><tspan x="254" y="741" class="b">Coating</tspan><tspan x="254" y="762">Application</tspan></text>
  <g aria-hidden="true" class="icon-o">
    <rect x="312" y="838" width="44" height="22" rx="4"/>
    <rect x="356" y="843" width="14" height="12"/>
    <rect x="373" y="840" width="4" height="18"/>
    <rect x="380" y="843" width="4" height="12"/>
    <rect x="322" y="858" width="14" height="36" rx="3"/>
    <rect x="326" y="818" width="22" height="20" rx="4"/>
  </g>
  <use href="#chev-k" x="397" y="860" width="16" height="20"/>

  <!-- Decommissioning & Abandonment -->
  <text class="sans cell-title on-blue"><tspan x="455" y="741" class="b">Decommissioning</tspan><tspan x="455" y="762" class="b">&amp; Abandonment</tspan></text>
  <g aria-hidden="true">
    <use href="#gear" x="500" y="842" width="40" height="40" class="icon-w"/>
    <circle cx="520" cy="862" r="7" class="cut-b"/>
    <rect x="498" y="880" width="80" height="16" class="icon-w"/>
    <rect x="540" y="820" width="40" height="30" rx="3" class="icon-w"/>
    <path d="M552 829 l16 12 M568 829 l-16 12" stroke="var(--navy)" stroke-width="4"/>
    <rect x="558" y="850" width="4" height="30" class="icon-w"/>
  </g>
  <use href="#chev-o" x="600" y="860" width="16" height="20"/>
</svg>
</section>

</body>
</html>
```